Need Business Card for our Indian Grocery Store

Industry/Entity Type

Grocery Store

Contact Information for Business Card

Manoj Baweja
Director

Store Locations:

Westbrook
482 Elm Parade
P: 03 9172 5843

Hollowmere
613 Carlow Road
P: 03 9238 6014

email: kvtmarts@mailnest.example

Requirements
Must have
• Our logo Colours

```html
<!DOCTYPE html>
<html lang="en">
<head>
<meta charset="utf-8">
<title>KVT Marts – Business Card</title>
<link href="https://fonts.googleapis.com/css2?family=Bitter:ital,wght@0,400;0,700;1,400&display=swap" rel="stylesheet">
<style>
  :root {
    --page: #ffffff;
    --card-grey: #d4d4d4;
    --brand-red: #e3150c;
    --ink: #111111;
    --white: #ffffff;
  }
  html, body {
    margin: 0;
    padding: 0;
    width: 1200px;
    height: 1200px;
    overflow: hidden;
    background: var(--page);
  }
  body {
    position: relative;
    font-family: "Bitter", Georgia, serif;
    color: var(--ink);
  }
  .card-front {
    position: absolute;
    left: 218px;
    top: 71px;
    width: 840px;
    height: 481px;
    background: var(--card-grey);
  }
  .card-back {
    position: absolute;
    left: 195px;
    top: 613px;
    width: 863px;
    height: 550px;
    background: var(--brand-red);
  }
  .person {
    position: absolute;
    left: 64px;
    top: 98px;
    line-height: 26px;
  }
  .person-name {
    font-size: 27px;
    font-weight: 400;
    margin: 0;
  }
  .person-role {
    font-size: 27px;
    font-weight: 700;
    margin: 0;
  }
  .email {
    position: absolute;
    left: 64px;
    top: 200px;
    display: flex;
    align-items: center;
    gap: 11px;
    font-size: 24px;
  }
  .icon { fill: var(--brand-red); flex: none; }
  .locations {
    position: absolute;
    left: 503px;
    top: 130px;
  }
  .locations-title {
    margin: 0 0 20px 26px;
    font-size: 23px;
    font-weight: 700;
  }
  .store {
    display: flex;
    align-items: center;
    gap: 8px;
    font-size: 24px;
    line-height: 24px;
    margin-bottom: 20px;
  }
  .phone {
    display: flex;
    align-items: center;
    gap: 10px;
    font-size: 24px;
    margin-bottom: 24px;
  }
  .brand-name {
    position: absolute;
    left: 0;
    right: 0;
    top: 200px;
    margin: 0;
    text-align: center;
    color: var(--white);
    font-size: 96px;
    font-weight: 700;
    letter-spacing: 2px;
    line-height: 1;
  }
  .tagline {
    position: absolute;
    left: 0;
    right: 0;
    top: 370px;
    display: flex;
    align-items: center;
    justify-content: center;
    gap: 12px;
    color: var(--white);
    font-size: 23px;
    font-style: italic;
  }
  .tagline .rule {
    width: 32px;
    height: 2px;
    background: var(--white);
  }
</style>
</head>
<body>
  <section class="card-front">
    <div class="person">
      <p class="person-name">Manoj Baweja</p>
      <p class="person-role">Director</p>
    </div>
    <div class="email">
      <svg class="icon" width="22" height="16" viewBox="0 0 22 16"><path d="M0 0h22v2l-11 7L0 2z M0 4.5l11 7 11-7V16H0z"/></svg>
      <span>kvtmarts@mailnest.example</span>
    </div>
    <div class="locations">
      <p class="locations-title">Store Locations:</p>
      <div class="store">
        <svg class="icon" width="18" height="24" viewBox="0 0 18 24"><path d="M9 0a9 9 0 0 1 9 9c0 6-9 15-9 15S0 15 0 9a9 9 0 0 1 9-9zm0 5a4 4 0 1 0 0 8 4 4 0 0 0 0-8z"/></svg>
        <span>Westbrook<br>482 Elm Parade</span>
      </div>
      <div class="phone">
        <svg class="icon" width="22" height="20" viewBox="0 0 22 20"><path d="M1 6c0-4 20-4 20 0v2h-5V6H6v2H1z M5 9h12l3 11H2z"/><circle cx="11" cy="14" r="3" fill="#d4d4d4"/></svg>
        <span>03 9172 5843</span>
      </div>
      <div class="store">
        <svg class="icon" width="18" height="24" viewBox="0 0 18 24"><path d="M9 0a9 9 0 0 1 9 9c0 6-9 15-9 15S0 15 0 9a9 9 0 0 1 9-9zm0 5a4 4 0 1 0 0 8 4 4 0 0 0 0-8z"/></svg>
        <span>Hollowmere<br>613 Carlow Road</span>
      </div>
      <div class="phone">
        <svg class="icon" width="22" height="20" viewBox="0 0 22 20"><path d="M1 6c0-4 20-4 20 0v2h-5V6H6v2H1z M5 9h12l3 11H2z"/><circle cx="11" cy="14" r="3" fill="#d4d4d4"/></svg>
        <span>03 9238 6014</span>
      </div>
    </div>
  </section>

  <section class="card-back">
    <p class="brand-name">KVT Marts</p>
    <div class="tagline">
      <span class="rule"></span>
      <span>Fresh Flavours Every Day</span>
      <span class="rule"></span>
    </div>
  </section>
</body>
</html>
```